Rail Industry Union looking for a flash Newsletter Design

Need a flash membership newsletter template that would effectively allow me to drag and drop each month/quarter or whatever frequency I choose.

I have my own I currently use (uploaded file), but looking for something modern that matches our new website design maybe (found at www.lwcmqe.asn.au).

I use 4 pages now, but would explore up to 6 moving forward.

Target Market(s)

Members and possible members

Industry/Entity Type

Union - Rail Industry

Requirements
Must have
• Easy clean layout, individual 'article' areas. Union logo or clear reference to the LWCM (Union)
Nice to have
• Style guide colours and fonts

```html
<!DOCTYPE html>
<html lang="en">
<head>
<meta charset="utf-8">
<title>LWCM Branch Update Newsletter</title>
<link href="https://fonts.googleapis.com/css2?family=Lato:ital,wght@0,400;0,700;0,900;1,400;1,700&display=swap" rel="stylesheet">
<style>
:root{
  --navy:#0f1a3d;
  --cream:#fcefdc;
  --white:#ffffff;
  --ink:#1f2230;
  --backdrop:#7d7d7d;
  --photo-warm:#e0a13a;
  --photo-blue:#3f6a9a;
  --photo-grey:#5c5c5c;
}
*{margin:0;padding:0;box-sizing:border-box}
html,body{width:1079px;height:1200px;overflow:hidden}
body{background:radial-gradient(ellipse at center,#9a9a9a 0%,var(--backdrop) 100%);font-family:'Lato',sans-serif;color:var(--ink);position:relative}
.page{position:absolute;width:475px;height:342px;background:var(--white);overflow:hidden;box-shadow:0 4px 14px rgba(0,0,0,.45)}
.col-left{left:51px}.col-right{left:553px}
.row-1{top:63px}.row-2{top:429px}.row-3{top:795px}
.page-head{position:absolute;left:0;top:0;width:100%;height:35px;background:var(--navy);color:var(--white);font-weight:700;font-size:19px;line-height:35px;padding-left:28px}
.badge{position:absolute;border-radius:50%;background:var(--white);border:2px solid var(--navy);display:flex;align-items:center;justify-content:center;color:var(--navy);font-weight:900;z-index:2}
.badge.small{width:42px;height:42px;right:20px;top:4px;font-size:9px}
.cream{position:absolute;top:35px;bottom:0;background:var(--cream)}
.art{position:absolute}
.ph{position:absolute}
p{margin:0}
/* cover */
.cover .page-head{text-align:center;padding-left:100px;font-size:18px}
.cover .badge{left:15px;top:8px;width:70px;height:70px;font-size:15px}
.issue-title{position:absolute;left:27px;top:94px;font-size:20px;font-weight:700;color:var(--navy);letter-spacing:-.2px}
.issue-list{position:absolute;left:29px;top:131px;list-style:none;font-size:9.6px;line-height:22px}
.meme-title{position:absolute;left:234px;width:241px;top:44px;text-align:center;font-size:20px;font-weight:700;color:var(--navy)}
.meme{left:273px;top:82px;width:164px;height:248px;background:linear-gradient(160deg,#f2c14e,var(--photo-warm) 60%,#c4622a)}
/* tax */
.tax-body{left:19px;top:55px;width:285px;font-size:7.4px;line-height:10.5px}
.tax-body a{color:var(--ink);text-decoration:underline}
.tax-photo{left:19px;top:176px;width:268px;height:149px;background:linear-gradient(120deg,#bfc7cc 0%,var(--photo-blue) 45%,#c9b36a 100%)}
.side-quote{font-style:italic;font-size:9.7px;line-height:14.2px;color:var(--ink)}
.power{font-weight:900;font-size:15px;line-height:19px;color:var(--ink)}
/* secretary */
.sec-col{top:46px;width:212px;font-size:7.6px;line-height:14.3px}
.sec-photo{left:254px;top:204px;width:115px;height:103px;background:linear-gradient(135deg,#9a9a9a,var(--photo-grey) 60%,#2a2a2a)}
.quote-box{left:348px;top:246px;width:127px;height:82px;background:var(--cream);padding:13px 8px 0 15px}
.quote-box h3{font-size:7.6px;font-weight:700;margin-bottom:6px}
.quote-box p{font-style:italic;font-size:6.2px;line-height:11.7px}
/* waging */
.war-body{left:12px;top:47px;width:292px;font-size:5.05px;line-height:10.45px}
.clip{position:absolute;background:linear-gradient(180deg,#dcdcdc,#a9a9a9)}
/* track */
.track-lead{left:13px;top:46px;font-size:10.8px;font-weight:700;color:var(--ink)}
.track-list{left:14px;top:71px;width:450px;list-style:none;font-size:7.05px;line-height:10.45px}
.track-list li::before{content:"• "}
/* award */
.aw-col{font-size:5.3px;line-height:7.9px}
.aw-head{font-size:13px;font-weight:700;color:var(--navy);line-height:16px}
.aw-list{list-style:none;font-size:5.3px;line-height:7.9px}
.aw-list li::before{content:"▫ "}
.caption{position:absolute;bottom:6px;left:0;width:100%;text-align:center;color:var(--white);font-style:italic;font-weight:700;font-size:4px;line-height:5px;padding:0 10px}
.foot{position:absolute;right:0;bottom:0;width:104px;height:36px;background:var(--navy);border-top-left-radius:30px;color:var(--white);font-size:3.6px;line-height:5.6px;padding:4px 0 0 24px;font-weight:700}
</style>
</head>
<body>

<!-- Cover -->
<section class="page cover col-left row-1">
  <div class="cream" style="left:234px;right:0"></div>
  <header class="page-head">LWCM WA CTA Branch Update</header>
  <div class="badge">LWCM</div>
  <h2 class="issue-title">INSIDETHISISSUE</h2>
  <ol class="issue-list">
    <li>1. Secretary’s Address</li>
    <li>2. Union Meme!</li>
    <li>3. A Quote with Relevance</li>
    <li>4. Out on Track</li>
    <li>5. Tax Time</li>
    <li>6. Waging War!</li>
    <li>7. Award-Dependent</li>
    <li>8. Super to Rise!</li>
    <li>9. Workplace Bullying</li>
  </ol>
  <h2 class="meme-title">Union Meme!</h2>
  <div class="ph meme" role="img" aria-label="Six-panel cartoon meme of a character calmly sitting in a burning room saying things are fine"></div>
</section>

<!-- Tax Time -->
<section class="page col-right row-1">
  <div class="cream" style="left:310px;right:0"></div>
  <header class="page-head">Tax Time</header>
  <div class="badge small">LWCM</div>
  <div class="art tax-body">
    <p>It is that time of the year again when everyone starts to get ready to visit their accountant. If you are a fully paid-up member for the 2020/2021 financial year, you can claim the full amount of $676 (or pro-rata thereof) with the Tax Office.</p>
    <p>That is right, your Union dues are 100% tax deductible, and you are entitled to claim them at tax time! Another reason to encourage a colleague to join.</p>
    <p>If you require an individual tax letter, please contact our office on 9000 4812.</p>
    <p>Alternatively, you can email Delia or Corinne at <a>general@lwcmqe.asn.au</a> and we will endeavour to get one emailed to you within 5 business days.</p>
    <p>Great news is that the new membership database, nearing completion, will send customised individual tax statements to each member automatically next FY.</p>
  </div>
  <div class="ph tax-photo" role="img" aria-label="Photo of wooden blocks spelling tax time beside a calculator, banknotes and a tax return form"></div>
  <p class="art side-quote" style="left:328px;top:59px;width:140px">“Met with the TRO GM to discuss safety concerns and alike with the premature opening of Northgate station &amp; triggered immediate safety improvements by TRO Safety.”</p>
  <h3 class="art power" style="left:328px;top:164px">THE POWER OF UNION</h3>
  <p class="art side-quote" style="left:328px;top:229px;width:140px">“Addressed concerns with RegionLink regarding use, access, and regulation to the audio and visual CCTV &amp; GPS capabilities contained within the Road Coaches.”</p>
</section>

<!-- Secretary -->
<section class="page col-left row-2">
  <header class="page-head">Secretary’s Address</header>
  <div class="badge small">LWCM</div>
  <p class="art sec-col" style="left:13px">Your employer, whether they are the CTA, Brightway, GSP, or Railmark, they have a business to run and as a business they are likely to face challenges that affect both their business and you as employees. Sometimes these challenges are small, such as introducing a new staff training program. Other times they are large, such as a loss of contract. Best practice employers examine and talk about these challenges with their staff and their respective unions. They aim for a genuine exchange of information and opinions and collaborate to reach solutions. Put simply, they consult. Consultation means asking for and considering employees’ and their unions views when making decisions. Cooperation means working together harmoniously to find solutions. Employers who take a consultative and cooperative approach still have the right to make the final decision on how to manage their business. Those employees, however, who are afforded the opportunity to be part of the process are more likely to accept change and are less likely to feel anxious or fearful. Being consulted about important decisions in the workplace can improve an employee’s engagement with their work. Simple really.</p>
  <p class="art sec-col" style="left:254px">Recently, and because of concerns raised by our Union, I received a letter signed by the A/Chief Executive Officer of the CTA that constitutes his commitment that “all Branches within that Division and indeed the CTA will comply with relevant consultative provisions within Industrial Agreements”. In addition, the letter identifies that he has “requested that relevant officers pay close attention to relevant provisions generally in regard to changes impacting on our operations with Linkway projects”. This is a step in the right direction, and a hopefully a positive sign of things to come.</p>
  <div class="ph sec-photo" role="img" aria-label="Portrait photo of the branch secretary"></div>
  <div class="art quote-box">
    <h3>A Quote with Relevance</h3>
    <p>“It took untold generations to get you where you are. A little gratitude might be in order.” – Dr. Alan Fenwick</p>
  </div>
</section>

<!-- Waging War -->
<section class="page col-right row-2">
  <div class="cream" style="left:310px;right:0"></div>
  <header class="page-head">Waging War!</header>
  <div class="badge small">LWCM</div>
  <p class="art war-body">Our Government’s belligerence over maintaining the State pay cap for its employees has convinced me to join forces with other public sector unions to take action on a united front. The Harlow Government capped public sector pay rises at a maximum $1000 a year in 2017, supposedly for four years. But straight after winning power again this year - thanks in no small part to the support of the State’s union movement - the Government is choosing to further extend the cap for another two years. I and other Union Leaders say that this betrayal is now an effective six year pay freeze, at a time the WA Government is running a $3 billion surplus. Recently, our Union, your delegates, and many members have worked very hard on negotiations. But while the subsequent enterprise agreements recently negotiated delivered several significant workplace gains, the $1000 pay cap has left many of you no doubt disillusioned with our State Government. Much because the Government’s wages policy has removed the ability to conduct genuine enterprise bargaining. We have got a State Government that is doing very well and has got one of the best economies in Australia, if not the world, on the back of the budget boost because of the booming iron ore price. Four years ago, we reluctantly accepted that the State’s books were not great, but I believe as members you have played your part for all West Australians. You have worked through the uncertainties of the pandemic and now you deserve to go back to genuine enterprise bargaining. I had considered stronger action recently in an attempt to break the Government’s pay stranglehold but had seen the cost borne by members in other unions that had tried to go it alone on that path. It became apparent that we must do something collectively, that all public sector unions must act together. We have joined the Public Service Alliance, where we can be part of a collective movement in 2022. The Public Service Alliance now includes our Union, UnionsCentral, the Allied Workers’ Union, Corrections Staff Union, State Educators’ Union, Health Care Staff Union, Fire Crews Union, and Professional Staff Network. With many others looking to jump onboard. Our Alliance covers more than 100,000 state public sector employees. As public sector unions we are committed to continuing the fight for genuine investment in public services - and the people who deliver them - but the current, restrictive, public sector wages policy is a significant barrier to this investment. So, we are promising a united campaign - a “Blue in’ 22” - to end the restrictive public sector wages policy, force a return to genuine enterprise bargaining in the public sector; and secure outcomes that represent a meaningful investment in public sector workers. Our Alliance will use all our resources, political, industrial, or organisational, to secure a successful outcome for all Alliance unions in the 2022 rounds of bargaining, as enough</p>
  <div class="clip" style="left:318px;top:44px;width:75px;height:64px" role="img" aria-label="Newspaper clipping headlined Waging war on $1000 pay rise"></div>
  <p class="art side-quote" style="left:319px;top:114px;width:148px;font-size:8.2px;line-height:12px">“It became apparent that we must do something collectively, that all public sector unions must act together.</p>
  <div class="ph" style="left:319px;top:155px;width:82px;height:55px;background:linear-gradient(135deg,#6b6f78,#2c2f38)" role="img" aria-label="Group photo of union leaders at the alliance launch"></div>
  <p class="art side-quote" style="left:320px;top:218px;width:148px;font-size:8.2px;line-height:12px">“So, we are promising a united campaign a “Blue in’ 22” - to end the restrictive public sector wages policy”</p>
  <div class="clip" style="left:319px;top:269px;width:71px;height:73px" role="img" aria-label="Newspaper opinion page clipping headlined Unions lift lid on wage cap"></div>
</section>

<!-- Out on Track -->
<section class="page col-left row-3">
  <header class="page-head">Out on Track</header>
  <div class="badge small">LWCM</div>
  <h3 class="art track-lead">Below are just some of the recent and current issues/matters dealt with by our Union:</h3>
  <ul class="art track-list">
    <li>Initiated enquiries and raised concerns with both the communication, and conduct of, health assessments by the CTA/OSH Group, particularly their blood sample consent form.</li>
    <li>Ensured our public sector members were aware of their ability to access the COVID vaccine during work hours.</li>
    <li>Supported numerous members through discipline investigations, including drafting responses to allegations, attending interviews, and viewing CCTV of incidents.</li>
    <li>Provided feedback and input on the new TRO Railcar Driver Agreement, negotiated payment terms for future training requirements related to Linkway for Urban Railcar Drivers, and commenced research for their upcoming Work Value Review</li>
    <li>Met with the TRO GM to discuss safety concerns and alike with the premature opening of Northgate station &amp; triggered immediate safety improvements by TRO Safety.</li>
    <li>Assisted a member with 5 days’ worth of their sick leave entitlement being recredited.</li>
    <li>Reviewed proposed roster changes for CTA Customer Service staff, provided feedback, and reviewed aggregate &amp; annual leave loading calculations.</li>
    <li>Met with Security Services Management to discuss numerous membership concerns resulting in positive changes to some previously issued Notices to Staff (NTS).</li>
    <li>Addressed concerns with the use of Relief Lines resulting in positive roster changes.</li>
    <li>Assisted a member to return to their previous substantive position of Transit Officer.</li>
    <li>Addressed concerns with RegionLink regarding use, access, and regulation to the audio and visual CCTV &amp; GPS capabilities contained within the Road Coaches.</li>
    <li>Referred and managed members’ interactions with industrial, family, criminal, and workers/criminal compensation lawyers.</li>
    <li>Attended the Public Service Alliance launch event &amp; gave a speech at the SEU’s State Council explaining the impact of the Wages Policy to LWCM members.</li>
    <li>Responded to emails, calls, and provided advice daily to countless members on a range of workplace topics and issues.</li>
    <li>Reviewed and provided feedback on the draft changes addressing customer service skills and knowledge related to ticketing and security requirements.</li>
    <li>Engaged in an extensive campaign to prevent mandatory in-cab surveillance legislation.</li>
  </ul>
</section>

<!-- Award-Dependent -->
<section class="page col-right row-3">
  <header class="page-head">Award-Dependent</header>
  <div class="badge small">LWCM</div>
  <p class="art aw-col" style="left:13px;top:49px;width:172px">The union movement recently won, effective July 1, a 2.5% pay increase for a quarter of all Australian workers through the Wage Review Panel’s annual minimum wage case, despite hardline opposition. Sadly, the Federal Government, most State Governments, and big business wanted pay cuts or freezes. This pay rise will raise the annual minimum wage to $40,175.20 and the hourly rate to $20.33 and will also flow through to those who are award-dependent, lifting the wages of 1 in 4 workers including our Brightway cleaner membership. Wage growth has remained effectively stagnant for 8 years</p>
  <h3 class="art aw-head" style="left:13px;top:140px">Super to Rise!</h3>
  <p class="art aw-col" style="left:13px;top:163px;width:172px">After a lifetime of work, all Australians deserve a comfortable retirement. For most people, superannuation will play an important part in helping secure a modest lifestyle. Thanks to the campaigning and hard work of unions, a system of compulsory superannuation began operating in 1992. As a result of further campaigning by unions, and their members, a previous federal government introduced laws that will see the minimum superannuation guarantee increase to 12%. As of July 1, 2021, superannuation will increase to 10%, and every year thereafter an additional 0.5%, until it finally reaches 12% by 2025</p>
  <h3 class="art aw-head" style="left:13px;top:250px">Workplace Bullying</h3>
  <p class="art aw-col" style="left:13px;top:273px;width:172px">Bullying is repeated and unreasonable behaviour that creates a risk to health and safety. Bullying behaviour can be as direct as making threats, swearing at, or abusing a worker, physical stand over tactics, or sexual harassment. It may also be more subtle and indirect.</p>
  <p class="art aw-col" style="left:213px;top:49px;width:240px">Wage suppression in our country needs to stop. Suppressing wages hurts the economic recovery and it hurts working people, their families, and communities. There can be no economic recovery without a wage’s recovery. Pay increases will be spent in local communities across the country and will help small and medium businesses as well as working people get back on their feet. Government needs to change their policies that are keeping wages low by supporting pay increases for their own workers, supporting more secure jobs, and changing laws to restore bargaining power to workers.</p>
  <div class="ph" style="left:213px;top:114px;width:159px;height:84px;background:linear-gradient(135deg,#3a4a63,#1b2336)" role="img" aria-label="Image of a hand placing banknotes beside rising bars showing superannuation guarantee increases">
    <p class="caption">Superannuation would not exist had it not been for the campaigns fought by union members in the 1970s and 1980s.</p>
  </div>
  <div class="ph" style="left:376px;top:114px;width:93px;height:84px;background:linear-gradient(135deg,#6e6e74,#2a2a30)" role="img" aria-label="Image with a no-bullying sign over the words workplace bullying">
    <p class="caption">Put a stop to workplace bullying!</p>
  </div>
  <div class="art" style="left:213px;top:212px;width:150px">
    <p class="aw-col">Bullying behaviour may take the following forms:</p>
    <ul class="aw-list">
      <li>aggressive or intimidating conduct;</li>
      <li>belittling or humiliating comments;</li>
      <li>spreading malicious rumours;</li>
      <li>teasing, practical jokes or ‘initiation ceremonies’;</li>
      <li>exclusion from work-related events;</li>
      <li>displaying offensive material;</li>
      <li>pressure to behave in an inappropriate manner;</li>
    </ul>
    <p style="font-size:7px;font-weight:700;margin:5px 0 1px">Bullying occurs when:</p>
    <ul class="aw-list">
      <li>a person (or a group) repeatedly behaves unreasonably towards a worker (or a group) at work; AND</li>
      <li>that unreasonable behaviour creates a risk to health and safety</li>
    </ul>
  </div>
  <p class="art" style="left:373px;top:212px;width:96px;font-size:4.3px;line-height:7.9px">Men and women at all levels of employment can be affected by bullying. Bullying behaviour can adversely affect the health and wellbeing of workers and may lead to stress-related illness, mental health issues and possibly workers’ compensation claims. Confronting a workplace bully can be a difficult and stressful task. For information on how to put a stop to workplace bullying please <b>visit: https://www.lwcmqe.asn.au/2021/06/25/put-a-stop-towork-place-bullying</b></p>
  <div class="foot">Line Workers &amp; Carriers Movement<br>Unit 4/18 Kestrel Road, Perth WA 6000<br>www.lwcmqe.asn.au<br>general@lwcmqe.asn.au<br>(08) 9000 4812</div>
</section>

</body>
</html>
```